Flyer-Design für Weihnachtsbäume als Dekoration
Zielgruppe
Wir bearbeiten Bleche nach Kundenvorgaben. Nebenbei stellen wir immer mal ein paar Dekoartikel
bzw. Sonderanfertigen her.
https://feinblechwerk-muster.de/
http://www.talbergwerk.de/
https://feinblechwerk-muster.de/aktuelles/image-broschuere/
Mit diesem Flyer wollen wir für unsere Weihnachtsbäume werben. Die Preise sind Endpreis inkl. Mehrwertsteuer.
Aufgabenstellung
Ich hab noch mehr Bildmaterial zur Verfügung.

```html
<!DOCTYPE html>
<html lang="de">
<head>
<meta charset="utf-8">
<title>Weihnachtsbäume – Varianten</title>
<link rel="stylesheet" href="https://fonts.googleapis.com/css2?family=Kaushan+Script&family=Oswald:wght@300;600&display=swap">
<style>
  :root {
    --page-bg: #e9e9e9;
    --frame-gold: #b8924f;
    --panel-gold: #d2bf86;
    --panel-gold-deep: #c7ae6c;
    --paper: #f6f6f7;
    --ink-light: #ffffff;
    --url-gold: #c9a957;
    --photo-a: #e4e2df;
    --photo-b: #8a7a68;
    --photo-c: #2b2a2c;
  }
  * { box-sizing: border-box; margin: 0; padding: 0; }
  html, body { width: 1200px; height: 800px; overflow: hidden; }
  body { background: var(--page-bg); position: relative; }

  .flyer {
    position: absolute; left: 270px; top: 70px;
    width: 660px; height: 660px;
    background: var(--paper);
    box-shadow: 0 12px 30px rgba(0,0,0,.12);
  }
  .frame-top { position: absolute; left: 0; top: 0; width: 660px; height: 16px; background: var(--frame-gold); }
  .frame-right { position: absolute; right: 0; top: 0; width: 16px; height: 570px; background: var(--frame-gold); }

  .price-panel {
    position: absolute; left: 0; top: 16px;
    width: 556px; height: 544px;
    background: linear-gradient(160deg, var(--panel-gold) 0%, var(--panel-gold-deep) 100%);
    padding: 40px 40px 0 44px;
    color: var(--ink-light);
  }
  .panel-title {
    font-family: "Kaushan Script", cursive;
    font-weight: 400; font-size: 40px; line-height: 1;
    margin-bottom: 10px;
  }
  .variant-list { list-style: none; }
  .variant {
    display: grid;
    grid-template-columns: 1fr 110px 96px;
    align-items: end;
    height: 38px;
    padding-bottom: 5px;
    border-bottom: 1px solid var(--ink-light);
    font-family: "Oswald", sans-serif;
  }
  .variant-name, .variant-height { font-weight: 300; font-size: 13px; letter-spacing: .2px; }
  .variant-price { font-weight: 600; font-size: 17px; text-align: right; transform: translateY(-12px); }

  .photo-strip {
    position: absolute; left: 556px; top: 16px;
    width: 88px; height: 544px;
    background: linear-gradient(180deg, var(--photo-a) 0%, var(--photo-b) 45%, var(--photo-c) 75%, var(--photo-a) 100%);
  }

  .footer-band { position: absolute; left: 0; top: 560px; width: 660px; height: 100px; background: var(--paper); }
  .site-box {
    position: absolute; right: 96px; top: 30px;
    border: 3px solid var(--url-gold);
    padding: 6px 22px;
    font-family: "Oswald", sans-serif; font-weight: 600;
    font-size: 22px; letter-spacing: .5px;
    color: var(--url-gold);
  }
</style>
</head>
<body>
  <article class="flyer">
    <div class="frame-top"></div>
    <div class="frame-right"></div>

    <section class="price-panel">
      <h1 class="panel-title">Varianten</h1>
      <ul class="variant-list">
        <li class="variant"><span class="variant-name">Baum, weiß beschichtet</span><span class="variant-height">Höhe: klein</span><span class="variant-price">25,00 €</span></li>
        <li class="variant"><span class="variant-name">Baum, weiß beschichtet</span><span class="variant-height">Höhe: 80cm</span><span class="variant-price">36,00 €</span></li>
        <li class="variant"><span class="variant-name">Baum, verzinkt</span><span class="variant-height">Höhe: 100cm</span><span class="variant-price">130,00 €</span></li>
        <li class="variant"><span class="variant-name">Baum, weiß beschichtet</span><span class="variant-height">Höhe: 120cm</span><span class="variant-price">90,00 €</span></li>
        <li class="variant"><span class="variant-name">Baum, verzinkt</span><span class="variant-height">Höhe: 120cm</span><span class="variant-price">150,00 €</span></li>
        <li class="variant"><span class="variant-name">Baum, doppelwandig, verzinkt</span><span class="variant-height">Höhe: 150cm</span><span class="variant-price">300,00 €</span></li>
        <li class="variant"><span class="variant-name">Baum, doppelwandig, verzinkt &amp; pulverbeschichtet</span><span class="variant-height">Höhe: 150cm</span><span class="variant-price">370,99 €</span></li>
        <li class="variant"><span class="variant-name">Baum, doppelwandig, Cortenstahl (Rostoptik)</span><span class="variant-height">Höhe: 150cm</span><span class="variant-price">335,00 €</span></li>
        <li class="variant"><span class="variant-name">Baum, doppelwandig, verzinkt</span><span class="variant-height">Höhe: 180cm</span><span class="variant-price">350,00 €</span></li>
        <li class="variant"><span class="variant-name">Baum, doppelwandig, verzinkt</span><span class="variant-height">Höhe: 230cm</span><span class="variant-price">430,00 €</span></li>
        <li class="variant"><span class="variant-name">Baum, doppelwandig, nicht verzinkt</span><span class="variant-height">Höhe: 230cm</span><span class="variant-price">280,00 €</span></li>
      </ul>
    </section>

    <div class="photo-strip" role="img" aria-label="Foto: Metall-Weihnachtsbaum als Dekoration mit Sternen und Kerzen"></div>

    <footer class="footer-band">
      <div class="site-box">FEINBLECHWERK-MUSTER.DE</div>
    </footer>
  </article>
</body>
</html>
```